VELOQUARD Stationery Design Project

I want a stationery design for a web development company consists of:
1- business card
2- Letter Head
3- small Envelope
4- Large Envelope

need a very clean professional simple design yet creative,

The company logo is attached
http://www.artpitchly.com/project-progress/designs.aspx?briefId=5173048&submissionId=73920416

logo font is sui generis rg (attached)
I would like to have the stationery text font to be helvetica font regular or light (can be changed)

I love the combination of cyan, black and grey colors
( will attach some recommended styles)

Industry/Entity Type

Business

Requirements
Should not have
• curves or waves

```html
<!DOCTYPE html>
<html lang="en">
<head>
<meta charset="utf-8">
<title>VELOQUARD Stationery</title>
<link href="https://fonts.googleapis.com/css2?family=Roboto:wght@300;400;500&display=swap" rel="stylesheet">
<style>
  :root {
    --bg: #ebebeb;
    --paper: #f4f4f4;
    --dark: #353535;
    --cyan: #2a9fd3;
    --grey: #8a8a8a;
    --ink: #3a3a3a;
  }
  * { box-sizing: border-box; margin: 0; padding: 0; }
  html, body { width: 1200px; height: 900px; overflow: hidden; }
  body { background: var(--bg); font-family: "Roboto", Helvetica, Arial, sans-serif; color: var(--ink); position: relative; }
  .piece { position: absolute; box-shadow: 0 2px 6px rgba(0,0,0,.12); }
  .wordmark { font-weight: 500; color: var(--cyan); letter-spacing: .06em; white-space: nowrap; }

  /* Letterhead */
  .letterhead { left: 252px; top: 112px; width: 331px; height: 470px; background: var(--paper); }
  .letterhead .wordmark { position: absolute; left: 28px; top: 28px; font-size: 10px; }
  .letterhead .sender { position: absolute; left: 243px; top: 25px; padding-left: 7px; border-left: 1px solid #bbb; font-size: 5.6px; line-height: 7px; width: 80px; height: 42px; }
  .letterhead .sender p + p { margin-top: 5px; }
  .letterhead .edge-tab { position: absolute; right: 0; top: 26px; width: 3px; height: 12px; background: var(--cyan); }
  .fold-mark { position: absolute; left: 0; width: 8px; height: 1px; background: #bbb; }
  .recipient { position: absolute; left: 37px; top: 89px; font-size: 6.2px; line-height: 7.8px; }
  .date { position: absolute; left: 37px; top: 162px; font-size: 6.2px; }
  .body-text { position: absolute; left: 37px; top: 184px; width: 271px; font-size: 6.1px; line-height: 7.8px; text-align: justify; }
  .body-text p + p { margin-top: 8px; }
  .signature { position: absolute; left: 37px; top: 403px; width: 62px; height: 20px; background: linear-gradient(90deg, #e4e6ee, #d8dbe8); }
  .signer { position: absolute; left: 37px; top: 428px; font-size: 6.2px; font-weight: 500; }

  /* Large envelope / folder */
  .folder { left: 642px; top: 90px; width: 391px; height: 495px; background: var(--dark); }
  .folder .sheet-edge { position: absolute; top: 0; bottom: 0; width: 1px; background: #2a2a2a; }
  .folder .edge-tab { position: absolute; left: 0; top: 452px; width: 5px; height: 14px; background: var(--cyan); }
  .folder .wordmark { position: absolute; left: 54px; top: 452px; font-size: 12px; }
  .folder .url-band { position: absolute; left: 143px; right: 2px; top: 455px; height: 15px; background: var(--cyan); color: #e8f6fc; font-size: 8px; letter-spacing: .08em; text-align: center; line-height: 15px; font-weight: 300; }

  /* Business cards */
  .card { width: 150px; height: 85px; left: 132px; overflow: hidden; }
  .card-front { top: 623px; background: var(--dark); }
  .card-front .edge-tab { position: absolute; left: 0; top: 67px; width: 2px; height: 7px; background: var(--cyan); }
  .card-front .wordmark { position: absolute; left: 11px; top: 66px; font-size: 6.5px; }
  .card-front .band { position: absolute; left: 77px; right: 0; top: 67px; height: 7px; background: var(--cyan); }
  .card-back { top: 732px; background: var(--paper); }
  .card-back .panel { position: absolute; left: 0; top: 0; width: 51px; height: 100%; background: var(--dark); }
  .card-back .band { position: absolute; left: 0; width: 51px; top: 66px; height: 7px; background: var(--cyan); }
  .card-back .name { position: absolute; left: 64px; top: 47px; font-size: 5px; font-weight: 500; }
  .card-back .title { position: absolute; left: 64px; top: 54px; font-size: 3.6px; color: var(--grey); }
  .card-back .contact { position: absolute; left: 101px; top: 47px; padding-left: 3px; border-left: 1px solid #ccc; font-size: 3.4px; line-height: 4.3px; }
  .card-back .contact p + p { margin-top: 3px; }
  .card-back .edge-tab { position: absolute; right: 0; top: 66px; width: 2px; height: 7px; background: var(--cyan); }

  /* Small envelope front */
  .envelope-front { left: 321px; top: 636px; width: 371px; height: 178px; background: var(--paper); }
  .envelope-front .wordmark { position: absolute; left: 15px; top: 15px; font-size: 13px; }
  .envelope-front .edge-tab { position: absolute; left: 0; top: 148px; width: 3px; height: 12px; background: var(--cyan); }
  .envelope-front .return-address { position: absolute; left: 16px; top: 148px; font-size: 6.2px; line-height: 7.6px; }

  /* Small envelope back */
  .envelope-back { left: 729px; top: 636px; width: 371px; height: 178px; background: var(--paper); }
  .envelope-back svg { position: absolute; left: 0; top: 0; }
  .envelope-back .wordmark { position: absolute; left: 0; right: 0; top: 25px; text-align: center; font-size: 10px; }
</style>
</head>
<body>

<section class="piece letterhead" aria-label="Letterhead">
  <div class="wordmark">VELOQUARD</div>
  <div class="sender">
    <p>18-40 Linden Row<br>Halbrook, NY 10990</p>
    <p>555-014-228<br>emarrow@veloquard.com<br>www.veloquard.com</p>
  </div>
  <div class="edge-tab"></div>
  <div class="fold-mark" style="top:156px"></div>
  <div class="fold-mark" style="top:312px"></div>
  <div class="recipient">Norvik GmbH<br>Anna Feldt<br>Ostwaldweg 14<br>4051 Talberg<br>Schweiz</div>
  <div class="date">Halbrook, March 26, 2016</div>
  <div class="body-text">
    <p>Lorem ipsum dolor sit amet, consectetur adipisicing elit, sed do eiusmod tempor incididunt ut labore et dolore magna aliqua. Ut enim ad minim veniam, quis nostrud exercitation ullamco laboris nisi ut aliquip ex ea commodo consequat.</p>
    <p>Duis aute irure dolor in reprehenderit in voluptate velit esse cillum dolore eu fugiat nulla pariatur. Excepteur sint occaecat cupidatat non proident, sunt in culpa qui officia deserunt mollit anim id est laborum.</p>
    <p>Sed ut perspiciatis unde omnis iste natus error sit voluptatem accusantium doloremque laudantium, totam rem aperiam, eaque ipsa quae ab illo inventore veritatis et quasi architecto beatae vitae dicta sunt explicabo.</p>
    <p>Nemo enim ipsam voluptatem quia voluptas sit aspernatur aut odit aut fugit, sed quia consequuntur magni dolores eos qui ratione voluptatem sequi nesciunt. Neque porro quisquam est, qui dolorem ipsum quia dolor sit amet, consectetur, adipisci velit, sed quia non numquam eius modi tempora incidunt ut labore et dolore magnam aliquam quaerat voluptatem.</p>
    <p>Ut enim ad minima veniam, quis nostrum exercitationem ullam corporis suscipit laboriosam, nisi ut aliquid ex ea commodi consequatur?</p>
    <p>Quis autem vel eum iure reprehenderit qui in ea voluptate velit esse quam nihil molestiae consequatur, vel illum qui dolorem eum fugiat quo voluptas nulla pariatur?</p>
    <p>Duis aute irure dolor in reprehenderit in voluptate velit esse cillum dolore eu fugiat nulla pariatur. Excepteur sint occaecat cupidatat non proident, sunt in culpa qui officia deserunt mollit anim id est laborum.</p>
  </div>
  <div class="signature" role="img" aria-label="Handwritten signature"></div>
  <div class="signer">Ellis Marrow</div>
</section>

<section class="piece folder" aria-label="Large envelope">
  <div class="sheet-edge" style="left:3px"></div>
  <div class="sheet-edge" style="left:10px"></div>
  <div class="sheet-edge" style="left:20px"></div>
  <div class="edge-tab"></div>
  <div class="wordmark">VELOQUARD</div>
  <div class="url-band">www.veloquard.com</div>
</section>

<section class="piece card card-front" aria-label="Business card front">
  <div class="edge-tab"></div>
  <div class="wordmark">VELOQUARD</div>
  <div class="band"></div>
</section>

<section class="piece card card-back" aria-label="Business card back">
  <div class="panel"></div>
  <div class="band"></div>
  <div class="name">Ellis Marrow</div>
  <div class="title">Vice President</div>
  <div class="contact">
    <p>555-014-228<br>emarrow@veloquard.com<br>www.veloquard.com</p>
    <p>18-40 Linden Row<br>Halbrook, NY 10990</p>
  </div>
  <div class="edge-tab"></div>
</section>

<section class="piece envelope-front" aria-label="Small envelope front">
  <div class="wordmark">VELOQUARD</div>
  <div class="edge-tab"></div>
  <div class="return-address">18-40 Linden Row<br>Halbrook, NY 10990</div>
</section>

<section class="piece envelope-back" aria-label="Small envelope back">
  <svg width="371" height="178" viewBox="0 0 371 178" aria-hidden="true">
    <polygon points="0,0 371,0 362,61 9,61" fill="var(--dark)"/>
  </svg>
  <div class="wordmark">VELOQUARD</div>
</section>

</body>
</html>
```